Pavlin Official Introduction Powerpoint presentation

We are into business of Co working/ Ready to move in 100% customised plug and play office space company. Having large multinational like Travorix, Ledgerwise, KDT etc as our customer using spaces .Need to get official PPT design for digital and print media. This should contain our product and services, locations, existing clients, testimonials, videos etc. The presentation has to be sent at the time of introduction of brand to potential customer so it has to cover all aspects in result leaving impact on the viewer where he should get inclined to do business with us.

Target Market(s)

Large multi national global organisations

Colors

Designer to choose colors to be used in the design.

Requirements
Must have
• Tag line : Kickstart your Way
• Crisp information, impactful images, testimonials, Design should speak luxury and class like a luxury 5 star hotel brand. We will provide photos of actual sites seperately. Use below link for photos of current t offices
• https://files.brelvanshare.com/folders/7-_QmTrkaWx4PzLoNvbd3ReUyHsKc2D5e?usp=sharing
• Please take reference for content from this file
• https://pages.brelvanshare.com/document/d/482mkfBwT-qL7Hj2RZVyG_5xxmNtaSpQ8Kdh4Jw3V/edit?usp=sharing
Nice to have
• Any new impactful thing, actual site pictures
• Use below link for photos of current t offices
Should not have
• Link to content: https://pages.brelvanshare.com/document/d/482mkfBwT-qL7Hj2RZVyG_5xxmNtaSpQ8Kdh4Jw3V/edit?usp=sharing
• Images: This folder has all images related Pavlin relevant to the presentation: https://files.brelvanshare.com/folders/3Qwemk9TjRR8Lfu4NnZp2Yc8-3H?usp=sharing

```html
<!DOCTYPE html>
<html lang="en">
<head>
<meta charset="utf-8">
<title>Layers of Service</title>
<link href="https://fonts.googleapis.com/css2?family=Asap:wght@300;400;500;600;700&display=swap" rel="stylesheet">
<style>
  :root {
    --coral: #eb7379;
    --panel: #c66064;
    --white: #ffffff;
    --soft-white: #fbeeee;
  }
  * { box-sizing: border-box; margin: 0; padding: 0; }
  html, body { width: 1200px; height: 675px; overflow: hidden; background: var(--coral); }
  body { font-family: "Asap", Arial, sans-serif; color: var(--white); }
  .slide { position: relative; width: 1200px; height: 675px; background: var(--coral); overflow: hidden; }

  .connector { position: absolute; left: 0; top: 0; z-index: 2; pointer-events: none; }

  .title {
    position: absolute; left: 265px; width: 600px; top: 90px;
    text-align: center; font-size: 56px; font-weight: 700; letter-spacing: 1px; line-height: 1;
  }
  .tagline {
    position: absolute; left: 165px; width: 800px; top: 160px;
    text-align: center; font-size: 26px; font-weight: 300; color: var(--soft-white);
  }
  .tagline strong { font-weight: 700; }

  .services { list-style: none; position: absolute; left: 138px; top: 0; }
  .service {
    position: absolute; left: 0; display: flex; align-items: center; gap: 24px;
    font-size: 27px; letter-spacing: 2.4px; font-weight: 400; white-space: nowrap;
    transform: translateY(-50%);
  }
  .service svg { width: 28px; height: 28px; flex: none; }

  .extras {
    position: absolute; left: 612px; top: 227px; width: 480px; height: 391px;
    background: var(--panel); border-radius: 36px;
  }
  .extras-heading {
    position: absolute; left: 36px; top: 31px; font-size: 21px; font-weight: 600; white-space: nowrap;
  }
  .extra {
    position: absolute; left: 49px; display: flex; align-items: flex-start; gap: 13px;
    font-size: 17px; line-height: 23px; font-weight: 300; color: var(--soft-white); width: 425px;
  }
  .extra span { white-space: nowrap; }
  .extra svg { width: 24px; height: 24px; flex: none; margin-top: -1px; }
  .extra b { font-weight: 500; color: var(--white); }

  svg.icon { fill: none; stroke: var(--white); stroke-width: 1.4; stroke-linecap: round; stroke-linejoin: round; }
</style>
</head>
<body>
<main class="slide">
  <svg class="connector" width="1200" height="675" aria-hidden="true">
    <g stroke="#fff" stroke-width="3" fill="none" stroke-dasharray="9 7">
      <path d="M292 123 H192 V210"/>
      <path d="M839 123 H984 V232"/>
    </g>
    <g stroke="#fff" stroke-width="3">
      <line x1="292" y1="113" x2="292" y2="133"/>
      <line x1="839" y1="113" x2="839" y2="133"/>
    </g>
    <circle cx="192" cy="218" r="10" fill="#fff"/>
    <circle cx="984" cy="240" r="6" fill="#fff"/>
  </svg>

  <h1 class="title">LAYERS OF SERVICE</h1>
  <p class="tagline">You <strong>focus on your growth</strong>, we take care of the rest.</p>

  <ul class="services">
    <li class="service" style="top:278px">
      <svg class="icon" viewBox="0 0 26 26"><rect x="3" y="6" width="20" height="13" rx="1.5"/><path d="M9 23h8M13 19v4"/><path d="M9 6a4 4 0 0 1 8 0"/><path d="M8 12h3v3M18 12h-3v3"/></svg>
      IT SERVICES
    </li>
    <li class="service" style="top:331px">
      <svg class="icon" viewBox="0 0 26 26"><circle cx="7" cy="10" r="3"/><path d="M2 22c0-4 2-6 5-6s5 2 5 6"/><rect x="11" y="5" width="14" height="12"/><path d="M15 15v-4M18 15v-6M21 15v-3"/></svg>
      ADMIN SERVICES
    </li>
    <li class="service" style="top:387px">
      <svg class="icon" viewBox="0 0 26 26"><circle cx="14" cy="5" r="2.5"/><path d="M10 12c0-2.5 2-4 4-4s4 1.5 4 4"/><rect x="3" y="12" width="21" height="4"/><path d="M5 16v8h17v-8M3 9h5v3"/></svg>
      RECEPTION SERVICES
    </li>
    <li class="service" style="top:443px">
      <svg class="icon" viewBox="0 0 26 26"><circle cx="13" cy="13" r="11"/><path d="M6 13l4-4 3 2 3-2 4 4-5 5-2-2-2 2z"/></svg>
      COMMUNITY SERVICES
    </li>
    <li class="service" style="top:499px">
      <svg class="icon" viewBox="0 0 26 26"><path d="M2 24l9-13 4 5 2-3 7 11z"/><path d="M11 11V2h6l-2 2 2 2h-6"/></svg>
      PARKING SERVICE
    </li>
    <li class="service" style="top:555px">
      <svg class="icon" viewBox="0 0 26 26" style="stroke-width:2.6"><path d="M13 4v18M4 13h18"/></svg>
      AND MORE...
    </li>
  </ul>

  <section class="extras">
    <h2 class="extras-heading">Plus all the things we can’t put a price on:</h2>

    <p class="extra" style="top:72px">
      <svg class="icon" viewBox="0 0 24 24"><rect x="2" y="2" width="13" height="19"/><path d="M5 6h7M5 9h7M5 12h4"/><rect x="11" y="13" width="11" height="7" rx="1"/><circle cx="16.5" cy="16.5" r="1.5"/></svg>
      <span><b>ONE BILL</b> for all office services.</span>
    </p>
    <p class="extra" style="top:110px">
      <svg class="icon" viewBox="0 0 24 24"><path d="M2 2v20h20"/><path d="M6 21v-5M10 21v-8M14 21v-10M18 21v-13"/><path d="M4 14l6-6 3 3 7-7"/></svg>
      <span><b>FLEXIBILITY</b> for growth.</span>
    </p>
    <p class="extra" style="top:147px">
      <svg class="icon" viewBox="0 0 24 24"><rect x="2" y="4" width="20" height="18" rx="1.5"/><path d="M2 9h20M6 2v4M12 2v4M18 2v4"/><path d="M9 13v6M12 13h3l-2 6"/></svg>
      <span><b>COMMUNITY</b> events.</span>
    </p>
    <p class="extra" style="top:185px">
      <svg class="icon" viewBox="0 0 24 24"><circle cx="12" cy="12" r="10"/><path d="M2 12h20M12 2c3 3 3 17 0 20M12 2c-3 3-3 17 0 20"/><circle cx="17" cy="15" r="4"/></svg>
      <span><b>ACCESS</b> to all our offices <b>ACROSS GEOGRAPHIES.</b></span>
    </p>
    <p class="extra" style="top:221px">
      <svg class="icon" viewBox="0 0 24 24"><rect x="5" y="2" width="11" height="20" rx="2"/><circle cx="5" cy="9" r="3"/><rect x="12" y="12" width="9" height="6" rx="1"/><path d="M15.5 13.5v3l2-1.5z"/></svg>
      <span><b>ALL</b> office <b>OPERATIONS</b> controlled via our<br><b>SMART APP.</b></span>
    </p>
    <p class="extra" style="top:281px">
      <svg class="icon" viewBox="0 0 24 24"><circle cx="12" cy="12" r="3.5"/><circle cx="12" cy="2.5" r="1.5"/><circle cx="12" cy="21.5" r="1.5"/><circle cx="2.5" cy="12" r="1.5"/><circle cx="21.5" cy="12" r="1.5"/><circle cx="5" cy="5" r="1.5"/><circle cx="19" cy="19" r="1.5"/><circle cx="19" cy="5" r="1.5"/><circle cx="5" cy="19" r="1.5"/><path d="M12 4v4.5M12 15.5V20M4 12h4.5M15.5 12H20M6 6l3.5 3.5M14.5 14.5L18 18M18 6l-3.5 3.5M9.5 14.5L6 18"/></svg>
      <span><b>NETWORK</b> with potential clients and investors.</span>
    </p>
    <p class="extra" style="top:318px">
      <svg class="icon" viewBox="0 0 24 24"><path d="M4 7h16l-1 15H5z"/><path d="M8 9V5a4 4 0 0 1 8 0v4"/><path d="M12 18l-3-3a1.8 1.8 0 0 1 3-2 1.8 1.8 0 0 1 3 2z"/></svg>
      <span><b>RETAIL OFFERS</b> for your employees from<br>major brands.</span>
    </p>
  </section>
</main>
</body>
</html>
```